Loftvane.ca Your Canadian Source for all your mortgage needs.

I need to get a fresh look on my current website. It is not currently a Wordpress site and i need to build a whole new site that i can do my editing in using Wordpress.
I need it built in a mobile or responsive theme.
There will be a secured application page which is critical.
I have 3 books written so i want to be able to have advertising spaces for promoting them and a landing page ( I can build my own landing pages)
I need the frame work of a professional theme with easy editing capabilities.
I have my own LOGOs which i would continue to use. The current site can be reviewed at www.loftvane.ca.
The front page could have a young couple near a nice house, open to suggestions.
I don't need a blog post to update but if it was on the sides of the pages I could use it. Something like a "Latest News" section.
I would like to have a Main page, Application Page, Resource page, Contact page, Calculator Page, a questions and answer page. Theses can be populated with the current information or I can add latter.
I want the main page to be a mini sales page so I can link to Posts on First Time Home Buyers, Refinance Options, Second Home or New purchase options.
I provide mortgages for people across Canada so i want the Canadian Flag incorporated
I like the colors to work with the logo colors on the current site

Target Market(s)

Canadian Mortgage Clients

Font styles to use
Sans Serif

Colors
3277b5
cadf82

Requirements
Must have
• Must work in a Wordpress Theme
• Please see Project description for more details
Nice to have
• Space to add banner ads for my books. I have 3 books written

```html
<!DOCTYPE html>
<html lang="en">
<head>
<meta charset="utf-8">
<title>Loftvane.ca – Mortgages across Canada</title>
<link href="https://fonts.googleapis.com/css2?family=Open+Sans:wght@400;600;700&display=swap" rel="stylesheet">
<style>
:root{
  --blue:#3277b5;
  --blue-dark:#1f5d9c;
  --green:#8cc03f;
  --green-soft:#cadf82;
  --ink:#333;
  --muted:#777;
  --rule:#e4e4e4;
  --footer:#2d2d2d;
  --footer-bottom:#222;
  --red:#d52b1e;
}
*{box-sizing:border-box;margin:0;padding:0}
html,body{width:773px;height:1200px;overflow:hidden}
body{font-family:"Open Sans",Arial,sans-serif;color:var(--ink);background:#fff;font-size:8px;line-height:1.5}

.site-header{height:38px;display:flex;align-items:center;justify-content:space-between;padding:0 70px}
.brand{display:flex;align-items:center;gap:6px;font-weight:700;font-size:13px;color:var(--blue)}
.brand-mark{width:14px;height:14px;background:var(--green)}
.main-nav{display:flex;gap:4px}
.main-nav a{font-size:8px;color:var(--ink);text-decoration:none;padding:4px 8px}
.main-nav a.active{background:#f0f0f0;border-bottom:2px solid var(--blue)}

.hero{height:332px;background:linear-gradient(180deg,#9fc3e3 0%,#c9b89c 35%,#a48e6f 60%,#5f8f3d 80%,#47762c 100%)}

.features{height:95px;background:var(--blue);display:flex;justify-content:center;gap:30px;padding-top:20px}
.feature{width:180px;display:flex;gap:10px;color:#fff}
.feature-icon{flex:none;width:32px;height:32px;border-radius:50%;background:#fff;display:flex;align-items:center;justify-content:center}
.feature h3{font-size:11px;font-weight:600;margin-bottom:2px}
.feature p{font-size:6.5px;opacity:.85;line-height:1.4}

.welcome{text-align:center;padding:26px 110px 0;height:170px}
.welcome h2{color:var(--blue);font-size:16px;font-weight:600;letter-spacing:.5px}
.welcome p{font-size:7px;color:var(--muted);margin:10px 0 14px}
.btn{display:inline-block;border:1px solid #bbb;background:#f4f4f4;color:var(--ink);font-size:7px;padding:3px 12px;border-radius:2px}

.books{display:flex;justify-content:center;gap:20px;height:130px}
.book{width:165px;height:112px;background:linear-gradient(#f6f6f6,#e3e3e3);border:1px solid #d8d8d8;display:flex;flex-direction:column}
.book-body{flex:1;display:flex;gap:8px;padding:10px}
.book-cover{width:36px;height:50px;background:linear-gradient(#6b8f3a,#2f5d8a)}
.book-title{font-size:9px;font-weight:600;color:var(--ink);line-height:1.3}
.book-cta{background:var(--green);color:#fff;font-size:6.5px;text-align:center;padding:4px}

.blog{padding:0 70px;height:215px}
.blog h2{text-align:center;color:var(--blue);font-size:15px;font-weight:600;margin-bottom:14px}
.posts{display:flex;gap:22px}
.post{flex:1}
.post-image{height:92px}
.post h4{color:var(--blue);font-size:8px;font-weight:600;margin-top:6px}
.post p{font-size:6.5px;color:var(--muted);line-height:1.4}

.site-footer{background:var(--footer);color:#ccc;height:172px;padding:18px 70px 0;display:flex;gap:26px}
.site-footer h5{color:#fff;font-size:7.5px;font-weight:600;margin-bottom:5px}
.site-footer ul{list-style:none;font-size:6.5px;line-height:1.7}
.col{width:70px}
.subscribe input{display:block;width:100px;height:13px;border:0;margin-bottom:5px}
.subscribe .go{display:inline-block;background:#555;color:#fff;font-size:6.5px;padding:2px 8px}
.social{display:flex;gap:4px;margin-bottom:10px}
.social span{width:13px;height:13px;border-radius:50%;background:var(--blue)}
.social span:nth-child(2n){background:#3b9fd8}
.social span:nth-child(3n){background:#c0392b}
.contact-line{display:flex;align-items:center;gap:5px;font-size:7px;margin-bottom:5px}

.bottom-bar{background:var(--footer-bottom);height:28px;display:flex;align-items:center;justify-content:space-between;padding:0 70px;color:#999;font-size:6.5px;position:relative}
.flag{position:absolute;left:350px;top:0;width:72px;height:28px;display:flex}
.flag i{flex:1;background:var(--red)}
.flag i:nth-child(2){flex:2;background:#fff}
.to-top{width:14px;height:14px;border-radius:50%;border:1px solid #777}
</style>
</head>
<body>

<header class="site-header">
  <div class="brand"><span class="brand-mark"></span>Loftvane Mortgages Inc.</div>
  <nav class="main-nav">
    <a class="active" href="#">Home</a><a href="#">Application</a><a href="#">Resource</a><a href="#">Calculator</a><a href="#">FAQ</a><a href="#">Contact</a>
  </nav>
</header>

<div class="hero" role="img" aria-label="Young couple with their child sitting on the lawn in front of a brick family home"></div>

<section class="features">
  <div class="feature">
    <span class="feature-icon"><svg width="14" height="14" viewBox="0 0 14 14"><path d="M2 12 L3 9 L10 2 L12 4 L5 11 Z" fill="var(--blue)"/></svg></span>
    <div><h3>Apply Online Now</h3><p>Start your secure application today and get a fast answer from our team.</p></div>
  </div>
  <div class="feature">
    <span class="feature-icon"><svg width="14" height="14" viewBox="0 0 14 14"><text x="7" y="11.5" text-anchor="middle" font-size="12" font-weight="700" fill="var(--blue)" font-family="Open Sans,Arial,sans-serif">$</text></svg></span>
    <div><h3>Save Thousands</h3><p>Compare rates across Canada and keep more money in your pocket.</p></div>
  </div>
  <div class="feature">
    <span class="feature-icon"><svg width="14" height="14" viewBox="0 0 14 14"><rect x="3" y="1.5" width="8" height="11" rx="1" fill="none" stroke="var(--blue)" stroke-width="1.4"/><rect x="4.5" y="3" width="5" height="2.5" fill="var(--blue)"/><rect x="4.5" y="7" width="2" height="2" fill="var(--blue)"/><rect x="7.5" y="7" width="2" height="2" fill="var(--blue)"/></svg></span>
    <div><h3>Mortgage Calculator</h3><p>Work out your payments and see what you can afford in minutes.</p></div>
  </div>
</section>

<section class="welcome">
  <h2>WELCOME TO LOFTVANE</h2>
  <p>Professional representation for you and your family is truly important to us. Finding the right mortgage is one of the biggest decisions you will make, and we help Canadians from coast to coast choose the product that suits their needs. Whether you are buying your first home, refinancing your current mortgage or planning a second property, our team walks you through every step with clear advice, competitive rates and a simple secure application.</p>
  <span class="btn">Welcome</span>
</section>

<section class="books">
  <div class="book"><div class="book-body"><div class="book-cover" role="img" aria-label="Book cover"></div><div class="book-title">Canadian First Time Home Buyers Resource Guide</div></div><div class="book-cta">Click to get book for a FREE copy</div></div>
  <div class="book"><div class="book-body"><div class="book-cover" role="img" aria-label="Book cover"></div><div class="book-title">Fix My Credit Now!</div></div><div class="book-cta">Click to get book for a FREE copy</div></div>
  <div class="book"><div class="book-body"><div class="book-cover" role="img" aria-label="Book cover"></div><div class="book-title">How To Save Thousands On Your Mortgage</div></div><div class="book-cta">Click to get book for a FREE copy</div></div>
</section>

<section class="blog">
  <h2>BLOG</h2>
  <div class="posts">
    <article class="post">
      <div class="post-image" role="img" aria-label="Couple reviewing home buying papers together" style="background:linear-gradient(135deg,#d9c9b3,#8a7a66)"></div>
      <h4>First Time Home Buyers</h4>
      <p>Everything you need to know before buying your first home, from saving a down payment to getting pre-approved with confidence. <b>More</b></p>
    </article>
    <article class="post">
      <div class="post-image" role="img" aria-label="Stack of coins next to a small model house" style="background:linear-gradient(135deg,#eef2f5,#9fb3c4)"></div>
      <h4>Refinance Options</h4>
      <p>Lower your rate, consolidate debt or access equity. Learn which refinance option fits your goals and your budget best. <b>More</b></p>
    </article>
    <article class="post">
      <div class="post-image" role="img" aria-label="House with a sold sign on the front lawn" style="background:linear-gradient(180deg,#b9d3ec,#9a8a78 55%,#5f8a3c)"></div>
      <h4>Second Home or New purchase options</h4>
      <p>Thinking about a cottage, rental or upsizing? Explore financing choices for your next property purchase today. <b>More</b></p>
    </article>
  </div>
</section>

<footer class="site-footer">
  <div class="col"><h5>Navigation</h5><ul><li>Home</li><li>Application</li><li>Resource</li><li>Calculator</li><li>FAQ</li><li>Contact</li></ul></div>
  <div class="col"><h5>More</h5><ul><li>Rates</li><li>Mortgage</li><li>Insurance</li><li>Credit</li><li>Blog</li></ul></div>
  <div class="col"><h5>More</h5><ul><li>Privacy Policy</li><li>Terms</li><li>Guidelines</li><li>Sitemap</li></ul></div>
  <div class="subscribe"><h5>Newsletter Subscribe</h5><input type="text" aria-label="Email"><span class="go">Subscribe</span></div>
  <div><h5>Connect with us</h5>
    <div class="social"><span></span><span></span><span></span><span></span><span></span><span></span></div>
    <div class="contact-line"><svg width="9" height="9" viewBox="0 0 10 10"><path d="M2 1 L4 1 L5 3 L4 4 Q5 6 6 6 L7 5 L9 6 L9 8 Q8 9 6 9 Q1 8 1 3 Q1 1 2 1 Z" fill="#ccc"/></svg>Call: 555 014 2290</div>
    <div class="contact-line"><svg width="9" height="9" viewBox="0 0 10 10"><rect x="1" y="2" width="8" height="6" fill="none" stroke="#ccc"/><path d="M1 2 L5 5.5 L9 2" fill="none" stroke="#ccc"/></svg>Email: info@loftvane.ca</div>
  </div>
</footer>

<div class="bottom-bar">
  <span>Copyright © 2014 Loftvane. All rights reserved.</span>
  <div class="flag" role="img" aria-label="Canadian flag"><i></i><i></i><i></i></div>
  <span class="to-top"></span>
</div>

</body>
</html>
```